The Brambury Firm

We need a new design for our letterhead and envelopes. We are a personal injury and criminal defense firm so we need something modern and clean, but more on the professional/traditional side. Our new logo has two colors and is attached to the file so we need something that works well with those colors/matches the design. The following information needs to be on the letterhead:
Phone: (555) 314-7265
Fax: (555) 419-6032
Toll-Free: (555) 736-1149
Post Office Box 4273
Ashvale, TQ 29458-4273
TQHarmClaimsDesk.example
PalmettoShieldCounsel.example

Target Market(s)

Clients, government agencies, other law firms

Industry/Entity Type

Legal

Font styles to use
Sans Serif
Other font styles liked:
• Arial

Colors

Designer to choose colors to be used in the design.

Requirements
Must have
• Must look professional and clean, modern
Nice to have
• I would like to see a design that works with the logo but does not distract from the content that will be printed on it
Should not have
• Too many colors or crazy designs.

```html
<!DOCTYPE html>
<html lang="en">
<head>
<meta charset="utf-8">
<title>The Brambury Firm — Stationery</title>
<link rel="stylesheet" href="https://fonts.googleapis.com/css2?family=Gelasio&family=Marcellus+SC&family=Marcellus&display=swap">
<style>
  :root {
    --navy: #2b3590;
    --red: #d2232a;
    --paper: #ffffff;
    --edge: #c9c9c9;
    --rule: #6f74b8;
    --body-text: #555555;
    --muted: #8a8a8a;
    --bg: #ffffff;
  }
  * { margin: 0; padding: 0; box-sizing: border-box; }
  html, body { width: 1200px; height: 1200px; overflow: hidden; background: var(--bg); }
  .canvas { position: relative; width: 1200px; height: 1200px; }

  .sheet { position: absolute; background: var(--paper); border: 1px solid var(--edge); overflow: hidden; }

  .wordmark {
    position: absolute;
    font-family: "Marcellus", serif;
    color: var(--navy);
    font-size: 22px;
    line-height: 1.1;
    white-space: nowrap;
    display: flex; align-items: center; gap: 8px;
  }
  .wordmark .dot { width: 12px; height: 12px; border-radius: 50%; background: var(--red); flex: none; }

  .address {
    position: absolute;
    font-family: "Marcellus SC", serif;
    color: var(--navy);
    font-size: 11.5px;
    line-height: 13px;
    white-space: nowrap;
  }
  .address .gap { height: 8px; }

  /* Letterhead */
  .letterhead { left: 46px; top: 114px; width: 753px; height: 976px; z-index: 1; }
  .letterhead .wordmark { left: 88px; top: 110px; }
  .letterhead .address { left: 524px; top: 71px; }
  .letter {
    position: absolute; left: 88px; top: 254px;
    font-family: "Gelasio", serif; font-size: 12px; color: var(--body-text);
    line-height: 19.8px; white-space: nowrap;
  }
  .letter p { margin-bottom: 19px; }
  .letter .greeting { margin-bottom: 33px; }
  .letter .closing { margin-top: 32px; margin-bottom: 67px; }
  .letter .signer { color: var(--navy); line-height: 18px; }
  .letter .role { color: var(--muted); line-height: 18px; }
  .rule { position: absolute; height: 1px; background: var(--rule); }
  .letterhead .rule { left: 79px; top: 898px; width: 598px; }
  .web-links {
    position: absolute; left: 0; right: 0; top: 927px; text-align: center;
    font-family: "Marcellus SC", serif;
    font-size: 13px; color: var(--red); letter-spacing: 0.3px; white-space: nowrap;
  }
  .web-links .sep { margin: 0 10px; }

  /* Envelope back */
  .envelope-back { left: 408px; top: 428px; width: 771px; height: 335px; z-index: 2; border-top: none; }
  .flap {
    position: absolute; left: 8px; top: 0; width: 754px; height: 100px;
    background: var(--navy); border-radius: 0 0 14px 14px;
    display: flex; align-items: center; justify-content: center;
  }
  .flap .web-links { position: static; color: #fff; font-size: 12.5px; }

  /* Envelope front */
  .envelope-front { left: 352px; top: 596px; width: 771px; height: 335px; z-index: 3; }
  .envelope-front .wordmark { left: 48px; top: 72px; }
  .envelope-front .rule { left: 51px; top: 262px; width: 720px; }
  .envelope-front .address { left: 52px; top: 280px; font-size: 10.5px; line-height: 12px; }
</style>
</head>
<body>
<main class="canvas">

  <section class="sheet letterhead" aria-label="Letterhead">
    <div class="wordmark"><span class="dot"></span>The Brambury Firm</div>
    <div class="address">
      <div>PO Box 4273</div>
      <div>Ashvale, TQ 29458-4273</div>
      <div class="gap"></div>
      <div>T: (555) 314-7265</div>
      <div>F: (555) 419-6032</div>
      <div>TF: (555) 736-1149</div>
    </div>
    <div class="letter">
      <p class="greeting">Dear Mr. Hale,</p>
      <p>Lorem ipsum dolor sit amet, consectetur adipiscing elit. Morbi tempor aliquet lacus, sit amet vehicula leo.<br>
      Phasellus ullamcorper magna felis, accumsan rhoncus nunc sagittis sed. Cum sociis natoque penatibus.<br>
      dis parturient montes, nascetur ridiculus mus. Pellentesque habitant morbi tristique senectus et netus.<br>
      Vestibulum aliquam augue eu mattis fermentum. Lorem ipsum dolor sit amet, consectetur adipiscing.<br>
      Cras suscipit odio at est adipiscing fermentum. Ut quis sem at quam tempor non eu quam. Lorem ipsum<br>
      consectetur adipiscing elit. Nulla facilisi. Cras suscipit odio at est adipiscing fermentum vitae sed.<br>
      Uteh quis sem at quam tempor non eu quam. Praesent dictum mi non egestas varius, nascetur ridiculus<br>
      ctetur nascetur ridiculus mus adipe.</p>
      <p>In vel accumsan sem, ac tincidunt quam. Donec sed lacus nec purus vehicula tincidunt at vel nisl<br>
      scelerisque. Morbi dictum, mi non egestas varius, augue nisl tempor sapien, ut pretium magna lorem<br>
      non consectetur purus. Proin sit amet sem ut lorem convallis aliquet vitae ac nibh sed dapibus quis<br>
      libero eu sapien vehicula bibendum. Aliquam erat volutpat.</p>
      <p class="closing">Thank You,</p>
      <div class="signer">Daniel Hale</div>
      <div class="role">President and Founder</div>
    </div>
    <div class="rule"></div>
    <div class="web-links">TQHarmClaimsDesk.example<span class="sep">|</span>PalmettoShieldCounsel.example</div>
  </section>

  <section class="sheet envelope-back" aria-label="Envelope back">
    <div class="flap">
      <div class="web-links">TQHarmClaimsDesk.example<span class="sep">|</span>PalmettoShieldCounsel.example</div>
    </div>
  </section>

  <section class="sheet envelope-front" aria-label="Envelope front">
    <div class="wordmark"><span class="dot"></span>The Brambury Firm</div>
    <div class="rule"></div>
    <div class="address">
      <div>PO Box 4273</div>
      <div>Ashvale, TQ 29458-4273</div>
    </div>
  </section>

</main>
</body>
</html>
```